Redfern Systems - Van Wrap

Project Overview
Redfern Systems is a fast-growing telecommunications company seeking a bold, professional van wrap design for our new fleet vehicle (Holvik Courier 310 Hauler). The wrap should clearly communicate our brand identity, highlight our core services, and create strong brand visibility on the road.
Objectives
Design a full vehicle wrap for a Holvik Courier 310 Hauler.
Establish instant brand recognition using our logo, brand colors, and clean design.
Communicate our core services in a clear, simple, and modern way.
Ensure the design is legible from a distance and looks professional across a fleet of vehicles.
Brand Identity
Company Name: Redfern Systems
Industry: Telecommunications / Low Voltage Solutions
Brand Attributes: Professional, Trustworthy, Innovative, Technical Expertise
Brand Colors: Blue, White, Grey (on a full black base)
Logo Files Provided: AI and PSD (attached)
Core Services to Highlight
Cameras
Access Control
Cabling & Networking
Audio / Visual
(We would like these paired with simple, modern icons for quick recognition.)
Van Content:
Should include the following:
Logo (attached)
Services:Cameras
Access Control
Cabling & Networking
Audio / Visual
Phone number: 800-526-3914
Website: www.redfernnetsys.example

```html
<!DOCTYPE html>
<html lang="en">
<head>
<meta charset="utf-8">
<title>Redfern Systems – Van Wrap</title>
<link rel="stylesheet" href="https://fonts.googleapis.com/css2?family=Montserrat:wght@500;800&family=Nunito:wght@800&display=swap">
<style>
  :root {
    --base-black: #1f1f20;
    --brand-blue: #4a9fe0;
    --brand-white: #f2f2f2;
    --brand-grey: #e4e4e4;
    --ink: #111111;
    --page: #ffffff;
  }
  html, body {
    margin: 0;
    padding: 0;
    width: 1200px;
    height: 1200px;
    overflow: hidden;
    background: var(--page);
  }
  .wrap-sheet {
    position: relative;
    width: 1200px;
    height: 1200px;
  }
  .panel { position: absolute; display: block; }
  .panel--side { left: 100px; top: 130px; }
  .panel--rear { left: 370px; top: 620px; }
  .brand-name {
    font-family: "Montserrat", sans-serif;
    font-weight: 500;
    fill: var(--brand-grey);
  }
  .services {
    font-family: "Nunito", sans-serif;
    font-weight: 800;
    fill: var(--brand-white);
  }
  .phone {
    font-family: "Montserrat", sans-serif;
    font-weight: 800;
  }
  .phone--dark { fill: var(--ink); }
  .phone--light { fill: var(--brand-white); }
  .website {
    font-family: "Nunito", sans-serif;
    font-weight: 800;
    fill: var(--brand-white);
    letter-spacing: 3px;
  }
  .website--rear { letter-spacing: 2px; }
  .base { fill: var(--base-black); }
  .band-blue { fill: var(--brand-blue); }
  .band-white { fill: var(--brand-white); }
  .stripe { fill: var(--base-black); }
  .brand-mark { fill: var(--brand-blue); }
</style>
</head>
<body>
<main class="wrap-sheet">

  <svg class="panel panel--side" width="1000" height="420" viewBox="0 0 1000 420" aria-label="Side panel wrap artwork">
    <defs>
      <radialGradient id="network-glow" cx="0.5" cy="0.4" r="0.6">
        <stop offset="0" stop-color="#5a5a5c"/>
        <stop offset="1" stop-color="#1f1f20"/>
      </radialGradient>
    </defs>
    <rect class="base" x="0" y="0" width="1000" height="420" rx="24"/>

    <rect x="640" y="20" width="330" height="230" rx="10" fill="url(#network-glow)"
          role="img" aria-label="Connected network nodes and lines motif"/>

    <rect class="brand-mark" x="70" y="92" width="70" height="70"/>
    <text class="brand-name" x="165" y="145" font-size="52">Redfern Systems</text>

    <polygon class="band-blue" points="40,262 480,262 560,330 40,330"/>
    <text class="services" x="60" y="290" font-size="22">• Cameras • Access Control</text>
    <text class="services" x="60" y="320" font-size="22">• Cabling &amp; Networking • Audio / Visual</text>

    <polygon class="band-blue" points="740,272 960,272 990,310 800,310"/>
    <polygon class="band-white" points="460,262 780,262 830,300 790,330 530,330"/>
    <text class="phone phone--dark" x="535" y="312" font-size="34">800-526-3914</text>

    <polygon class="band-blue" points="280,362 820,362 820,392 280,392"/>
    <g class="stripes">
      <polygon class="stripe" points="600,362 618,362 638,392 620,392"/>
      <polygon class="stripe" points="640,362 658,362 678,392 660,392"/>
      <polygon class="stripe" points="680,362 698,362 718,392 700,392"/>
      <polygon class="stripe" points="720,362 738,362 758,392 740,392"/>
      <polygon class="stripe" points="760,362 778,362 798,392 780,392"/>
    </g>
    <text class="website" x="292" y="386" font-size="19">redfernnetsys.example</text>
  </svg>

  <svg class="panel panel--rear" width="460" height="420" viewBox="0 0 460 420" aria-label="Rear doors wrap artwork">
    <rect class="base" x="0" y="0" width="460" height="420" rx="22"/>

    <rect x="10" y="50" width="85" height="200" rx="8" fill="url(#network-glow)"
          role="img" aria-label="Connected network nodes motif, left"/>
    <rect x="365" y="50" width="85" height="260" rx="8" fill="url(#network-glow)"
          role="img" aria-label="Connected network nodes motif, right"/>

    <polygon class="band-blue" points="30,0 430,0 360,45 100,45"/>
    <text class="phone phone--light" x="230" y="34" font-size="28" text-anchor="middle">800-526-3914</text>

    <rect class="brand-mark" x="195" y="95" width="70" height="70"/>
    <text class="brand-name" x="230" y="225" font-size="30" text-anchor="middle">Redfern Systems</text>

    <rect class="band-blue" x="20" y="320" width="420" height="56"/>
    <text class="services" x="230" y="343" font-size="19" text-anchor="middle">• Cameras • Access Control</text>
    <text class="services" x="230" y="368" font-size="19" text-anchor="middle">• Cabling &amp; Networking • Audio / Visual</text>

    <polygon class="band-blue" points="20,384 400,384 420,410 20,410"/>
    <polygon class="stripe" points="300,384 318,384 335,410 317,410"/>
    <polygon class="stripe" points="332,384 350,384 367,410 349,410"/>
    <polygon class="stripe" points="364,384 382,384 399,410 381,410"/>
    <text class="website website--rear" x="30" y="404" font-size="16">redfernnetsys.example</text>
  </svg>

</main>
</body>
</html>
```